A Book Cover For a Book Called "Tamsire"

Attached are two files for the ISBN bar graph for the print version of the cover! Same image, just two different formats.
Updates

Project Deadline Extended Reason: We'd like to see a few more designs, and work with a few of the designs already submitted. Added Tuesday, October 24, 2017

Target Market(s)

young adult female, parents

Colors

Designer to choose colors to be used in the design.

```html
<!DOCTYPE html>
<html lang="en">
<head>
<meta charset="utf-8">
<title>Tamsire – Book Cover</title>
<link rel="stylesheet" href="https://fonts.googleapis.com/css2?family=Playfair+Display:wght@400;700;900&display=swap">
<style>
  :root {
    --navy-deep: #07062a;
    --navy: #100d3d;
    --plum: #3a2548;
    --stage-grey: #8d8c97;
    --floor-grey: #4c4a58;
    --ink-light: #f4f3f8;
    --ink-soft: #e2e1ea;
    --paper: #ffffff;
  }
  * { margin: 0; padding: 0; box-sizing: border-box; }
  html, body {
    width: 1200px;
    height: 914px;
    overflow: hidden;
    background: var(--navy-deep);
  }
  .cover {
    position: relative;
    width: 1200px;
    height: 914px;
    overflow: hidden;
    font-family: "Playfair Display", Georgia, serif;
    color: var(--ink-light);
  }
  .cover-art {
    position: absolute;
    inset: 0;
    background:
      radial-gradient(ellipse 260px 420px at 930px 430px, rgba(190,188,200,0.55), transparent 75%),
      radial-gradient(ellipse 520px 260px at 760px 720px, rgba(110,106,122,0.55), transparent 80%),
      radial-gradient(ellipse 300px 200px at 520px 330px, rgba(90,50,95,0.45), transparent 80%),
      linear-gradient(180deg, var(--navy-deep) 0%, var(--navy) 45%, var(--floor-grey) 72%, var(--navy-deep) 100%);
  }
  .back-quote {
    position: absolute;
    left: 29px;
    top: 32px;
    font-size: 27px;
    font-weight: 400;
  }
  .back-blurb {
    position: absolute;
    left: 24px;
    top: 134px;
    width: 528px;
    font-size: 18.4px;
    line-height: 25.5px;
    text-align: justify;
    text-indent: 76px;
    color: var(--ink-soft);
  }
  .back-blurb strong { font-weight: 900; color: var(--ink-light); }
  .author-photo {
    position: absolute;
    left: 26px;
    top: 458px;
    width: 205px;
    height: 259px;
    background: var(--paper);
  }
  .author-bio {
    position: absolute;
    left: 242px;
    top: 482px;
    width: 322px;
    font-size: 20.5px;
    line-height: 27.2px;
    text-align: justify;
    color: var(--ink-soft);
  }
  .front-subtitle {
    position: absolute;
    left: 676px;
    top: 176px;
    font-size: 30px;
    line-height: 40px;
    font-weight: 400;
  }
  .front-title {
    position: absolute;
    left: 670px;
    top: 252px;
    font-size: 104px;
    line-height: 1;
    font-weight: 900;
    letter-spacing: -2px;
    color: var(--paper);
  }
</style>
</head>
<body>
  <main class="cover">
    <div class="cover-art" role="img" aria-label="Photograph of a ballerina's legs en pointe in satin shoes on a worn wooden stage floor, in dark navy and grey tones"></div>

    <p class="back-quote">"A quote from the book"</p>

    <p class="back-blurb"><strong>Lorem ipsum dolor sit amet, consetetur sadipscing elitr, sed diam nonumy eirmod tempor</strong> invidunt ut labore et dolore magna aliquyam erat, sed diam voluptua. At vero eos et accusam et justo duo dolores et ea rebum. Stet clita kasd gubergren, no sea takimata sanctus est Lorem ipsum dolor sit amet. Lorem ipsum dolor sit amet, consetetur sadipscing elitr, sed diam nonumy eirmod tempor invidunt ut labore et dolore magna aliquyam erat, sed diam voluptua. At vero eos et accusam et justo duo dolores et ea rebum. Stet clita kasd gubergren, no sea takimata sanctus est Lorem ipsum dolor sit amet.</p>

    <div class="author-photo"></div>

    <p class="author-bio">Lorem ipsum dolor sit amet, consetetur sadipscing elitr, sed diam nonumy eirmod tempor invidunt ut labore et dolore magna aliquyam erat, sed diam voluptua. At vero eos et accusam et justo duo dolores et ea rebum.</p>

    <p class="front-subtitle">a memoir<br>by Clara Voss with Nina Hale</p>

    <h1 class="front-title">TAMSIRE</h1>
  </main>
</body>
</html>
```